Ridgeline Build Network Inc. Letterhead

Creation of attractive and eye catching letterhead for a business start-up for the construction industry. Letterhead must relate to construction, but avoid standard hammer and tools in the design.
Updates

I forgot to add some details, sorry about that. Some pertinent info: Ph: 916-555-0148 ridgelinebuildnet.example 487 Willowmere Ave, Ste 210 Folsom, CA 95699 info@ridgelinebuildnet.example not sure if slogan should be in there" “Connecting construction professionals to create a purpose driven industry.” must be able to be used in word. Thanks!

```html
<!DOCTYPE html>
<html lang="en">
<head>
<meta charset="utf-8">
<title>Ridgeline Build Network Inc. Letterhead</title>
<link rel="stylesheet" href="https://fonts.googleapis.com/css2?family=Open+Sans:wght@400;600;700&family=Arimo:wght@700&display=swap">
<style>
  :root {
    --brand-red: #bb0a0e;
    --brand-navy: #0d1a52;
    --paper: #ffffff;
    --backdrop: #ececee;
    --body-text: #3a3a3a;
    --heading-text: #1b1b1b;
    --signature-tone: #d9d9de;
  }
  * { margin: 0; padding: 0; box-sizing: border-box; }
  html, body { width: 1200px; height: 784px; overflow: hidden; }
  body {
    background: var(--backdrop);
    font-family: "Open Sans", Arial, sans-serif;
    position: relative;
  }
  .letterhead {
    position: absolute;
    left: 335px;
    top: 20px;
    width: 530px;
    height: 744px;
    background: var(--paper);
    box-shadow: 0 2px 10px rgba(0,0,0,0.12);
    overflow: hidden;
  }
  .header-swoosh { position: absolute; left: 0; top: 0; width: 530px; height: 260px; }
  .contact-block {
    position: absolute;
    right: 22px;
    top: 8px;
    text-align: right;
    color: #fff;
    font-size: 7px;
    line-height: 11px;
  }
  .contact-line { display: flex; justify-content: flex-end; align-items: center; gap: 4px; }
  .contact-icon { width: 7px; height: 7px; }
  .brand-name {
    position: absolute;
    left: 30px;
    top: 222px;
    display: flex;
    align-items: center;
    gap: 7px;
    color: var(--brand-navy);
    font-family: "Open Sans", Arial, sans-serif;
    font-weight: 700;
    font-size: 12px;
    letter-spacing: 1.5px;
    text-transform: uppercase;
  }
  .brand-square { width: 10px; height: 10px; background: var(--brand-red); }
  .letter-body {
    position: absolute;
    left: 62px;
    top: 282px;
    width: 410px;
    color: var(--body-text);
    font-size: 10.5px;
    line-height: 15px;
  }
  .salutation {
    font-family: "Arimo", Arial, sans-serif;
    font-weight: 700;
    font-size: 13px;
    color: var(--heading-text);
    margin-bottom: 10px;
  }
  .letter-body p { margin-bottom: 14px; }
  .signature-area {
    width: 96px;
    height: 40px;
    margin-top: 6px;
    margin-left: 70px;
    background: linear-gradient(90deg, var(--signature-tone), #eeeef1);
    border-radius: 4px;
  }
  .footer-band {
    position: absolute;
    left: 0;
    bottom: 0;
    width: 100%;
    height: 50px;
    background: var(--brand-navy);
    display: flex;
    align-items: center;
    padding-left: 40px;
    gap: 8px;
    color: #fff;
  }
  .footer-pin { width: 12px; height: 16px; }
  .footer-company { font-size: 9px; font-weight: 700; line-height: 12px; }
  .footer-address { font-size: 8px; line-height: 11px; }
</style>
</head>
<body>
  <main class="letterhead">
    <svg class="header-swoosh" viewBox="0 0 530 260" aria-hidden="true">
      <path d="M0 0 H530 V42 C370 62 160 110 0 205 Z" fill="var(--brand-red)"/>
      <path d="M530 42 V64 C360 82 150 128 0 212 V205 C160 110 370 62 530 42 Z" fill="var(--brand-navy)"/>
    </svg>

    <div class="contact-block">
      <div class="contact-line">916-555-0148
        <svg class="contact-icon" viewBox="0 0 10 10"><path d="M2 1 L4 1 L5 3.5 L3.8 4.5 Q4.8 6.3 5.6 6.2 L6.5 5 L9 6 L9 8 Q5 9.5 1 3 Z" fill="#fff"/></svg>
      </div>
      <div class="contact-line">info@ridgelinebuildnet.example
        <svg class="contact-icon" viewBox="0 0 10 10"><rect x="1" y="2.5" width="8" height="5.5" fill="#fff"/><path d="M1 2.5 L5 6 L9 2.5" stroke="var(--brand-red)" stroke-width="0.8" fill="none"/></svg>
      </div>
      <div class="contact-line">ridgelinebuildnet.example
        <svg class="contact-icon" viewBox="0 0 10 10"><circle cx="5" cy="5" r="4" fill="#fff"/></svg>
      </div>
    </div>

    <div class="brand-name"><span class="brand-square"></span>Ridgeline Build Network</div>

    <section class="letter-body">
      <div class="salutation">Dear Mr. Avery,</div>
      <p>Lorem Ipsum is simply dummy text of the printing and typesetting industry. Lorem Ipsum has been the industry's standard dummy text ever since the 1500s, when an unknown printer took a galley of type and scrambled it to make a type specimen book. It has survived not only five centuries, but also the leap into electronic typesetting, remaining essentially unchanged.</p>
      <p>The standard chunk of Lorem Ipsum used since the 1500s is reproduced below for those interested. Sections 1.10.32 and 1.10.33 from "de Finibus Bonorum et Malorum" by Cicero are also reproduced in their exact original form, accompanied by English versions from the 1914 translation by H. Rackham</p>
      <p>Lorem Ipsum is simply dummy text of the printing and typesetting industry. Lorem Ipsum has been the industry's standard dummy text ever since the 1500s, when an unknown printer took a galley of type and scrambled it to make a type specimen book. It has survived not only five centuries, but also the leap into electronic typesetting, remaining essentially unchanged. It was popularised in the</p>
      <p>The standard chunk of Lorem Ipsum used since the 1500s is reproduced below for those interested. Sections 1.10.32 and 1.10.33 from "de Finibus Bonorum et Malorum" by Cicero are also reproduced in their exact original form, accompanied by English versions from the 1914 translation by H. Rackham</p>
      <p>The standard chunk of Lorem Ipsum used since the 1500s is reproduced below for those interested. Sections 1.10.32 and 1.10.33 from "de Finibus Bonorum et Malorum" by Cicero are</p>
      <div class="signature-area" role="img" aria-label="Handwritten signature of the sender"></div>
    </section>

    <footer class="footer-band">
      <svg class="footer-pin" viewBox="0 0 12 16" aria-hidden="true"><path d="M6 0 C2.7 0 0 2.6 0 5.8 C0 10 6 16 6 16 C6 16 12 10 12 5.8 C12 2.6 9.3 0 6 0 Z" fill="#fff"/><circle cx="6" cy="5.8" r="2.2" fill="var(--brand-navy)"/></svg>
      <div>
        <div class="footer-company">Ridgeline Build Network Inc.</div>
        <div class="footer-address">Po.box 201, Street Name, City Name, Zip Code :00000</div>
      </div>
    </footer>
  </main>
</body>
</html>
```